Mobile Repair Service on location needs a Web Design

We are starting a new mobile device repair service called Gadget Haven and our website needs a design!

Hello Designers!
First, we'd like to make clear this is more than a simple web design contest, we want the designers to create an idea. We want someone who can create the whole theme of the service's we provide. We want someone that can help design our visual branding, help us communicate a sentiment. And we are willing to pay for that.

Who are we?
Our company is based in Rotterdam, the Netherlands. We provide different services for all kinds of electronic devices. The kind of services we provide are, among other things, installations of hardware and software and the repair of broken or malfunctioning devices.
We are starting a new service that offers mobile device repairs on location, be it at the home of our customers, their office, or any other place. Just give us the address and we will come to you for the repair job. This is also our main USP. We have multiple skilled engineers who drive trough the country on a daily basis and can be on location within a working day. Repair is done immediately onsite while the customer waits. At this stage we will start with the smartphone product-group within the mobile devices. In a second phase we might also add tablets.
People don't want to be without their phone for weeks because of some parts that needed to be ordered by a repair center they had to sent their phone to. We offer a fully functional mobile repair center in the form of specially customized vans. These vans have all the tools and utilities needed by our engineers to safely repair your mobile device. Your phone is being repaired directly in front of you, the next business-day, on a location you desire.

For this new service we are creating a website called Gadget Haven. The website needs a story and matching design and this is where you come in. We are not looking for a simple template design we can get from any place. We need a story. We want you to create an idea, build a unique theme or vision that helps sell the product/service. This goes beyond the design of the website. We need the whole package, the design you are creating needs to have returning elements like icons, color use, images, maybe even characters etc. You name it! There needs to be a common thread in the design so we can reuse elements in, for example, the email templates, the work order or receipt we give to our customers (we may contact the winner of the contest to design these for us as well!).

The name 'Gadget Haven' is chosen. Haven (short for rehabilitate) has a bold and playful tone to it and the design needs to reflect the name. So we're looking for a somewhat playful and cheeky design. Definitely not too serious and definitely modern. We already got a logo that we love and that fit's this description (see attached design documents for the logo). It's bold, powerful and fun. Our web design needs to reflect this as well and has to fit in with our logo.
We would really like it if the design somehow incorporates elements that highlight our unique selling points (repairs on location, we come to you etc.). We would really like some form of story telling in the design. Think clumsy people breaking their phones. Teenagers in tears because they have no access to their friends. People nowadays have the need to always be 'connected'. What happens when your phone is broken or malfunctioning? We're handling tech, we are nerds and a little bit weird, but we're professionals and here to help you with your problem. The sentiment Wire Troop tries to communicate is something we really like. We're looking for fresh idea's, anything goes!

In an overview all Unique Selling Points of the Gadget haven service:
- Professional service on location. Don’t ship to us we will come to you!
- Clear pricing upfront. No hidden cost.
- Next business-day repair.
- Backed by a professional call center open 12 hours a day and open on a Saturday as well
- Backed by a professional repair center with more then 12 years of experience
- Repair is done by certified engineers
- 1 year warranty on the repair

The process:
The main function of our website will be for customers to make a repair request. A customer will visit our website and can make a repair request immediately by going through a 'request-order-flow'. In this flow he or she will need to fill in some forms and can select wich type/model/brand of mobile device he or she has and what parts need to be repaired. After a request is placed we will call the customer back (within an hour) for a short intake and to set a date/time and location. Our engineer will meet the customer at the specified location and will repair the device onsite in one of our mobile repair centers, which is a specialized van equipped with all the tools needed for device restorations.
So in short the steps are:
- Choose your device and repair job
- Place the order
- Get a callback within the hour
- Set date and location
- We will come to you.

Website functionality:
Our website is our main form of communication. So the sentiment we want to communicate needs be reflected in the design. We need a main/front page designed (preferably a long scrolling page design) containing:
1. Customers will be able to request a repair job directly on our website. So there will need to be a prominent button/link at the top of our main page that will bring the customer to this 'request-order-flow'. This is the main flow which needs to be full focus on the front page. All other items are secondary.
2. The general information of who we are and what we do, and why the customer should choose us. Preferably in short bullet-point type keywords/sentences with icons or other visual cues. See our unique selling points to get an idea of the information that will be displayed here.
3. There needs to be a section that will explain the process (see above) of a repair request step-by- step, again in brief short key sentences and with (custom) icons.
4. There needs to be a section that explains to the customer he/she can always contact us if they are not sure what the problem is with their device, and for this reason are not sure what repair request they should order.
5. We want to implement some functionality that display customer ratings or customer reviews. So there needs to be room for some kind of widget of plugin we're going to implement which shows these reviews.
6. A 'For business section' where we will explain all the options we provide for corporate clients.
7. Social media links.
8. There needs to be a menu with buttons that leads to the all sections described in the previous points.

For now, we need a design for our front page. In the second phase, when we have picked our winner, we may ask the winner to design the page(s) for our request workflow as well.

EDIT:
Finally, we have a very specific order in mind for the different segments of our website. We would like you to add some more segments that were not in our original brief as well:

1. Top header with order/request button. (should instantly make clear our main USP, we do repairs on location)
2. Our process
3. Our unique selling points / why choose us
4. The kind of repairs we do (broken screens, broken batteries, water damage, broken camera's, no sound etc.)
5. A 'meet our team' section, where we introduce some of our engineers
6. A 'contact us for any questions' section/
7. Testimonials/user reviews
8. A section where we show key performance indicators
9. 'For businesses' sections
10.'Subscribe for newsletter' field
11. Social media buttons

Industry/Entity Type

It Service

Number of Pages Required

1 page

Font styles to use
Sans Serif

Requirements
Must have
• a main/front page, design only
• custom icons/images for banners, adverts online and in print (high res)
Nice to have
• Storytelling in our design.
• Design that fits with our brand new logo.
• Elements like icons to have a flat design.
• Keep in mind that the website will need to be responsive when designing! (Ideally provide an example of the mobile design as well)
• Create a fun and trustworthy feeling.

```html
<!DOCTYPE html>
<html lang="en">
<head>
<meta charset="utf-8">
<title>Gadget Haven – Mobile Repair On Location</title>
<link rel="stylesheet" href="https://fonts.googleapis.com/css2?family=Roboto:wght@300;400;500;700&family=Oswald:wght@600&family=Lato:wght@300;400&display=swap">
<style>
:root{
  --orange:#e95d24;
  --orange-dark:#d24f1a;
  --ink:#222;
  --text:#444;
  --muted:#777;
  --dark:#1b1b1b;
  --white:#fff;
  --rule:#ddd;
  --map:#6d6d6d;
  --body:'Roboto',Arial,sans-serif;
}
*{margin:0;padding:0;box-sizing:border-box}
html,body{width:1200px;height:2757px;overflow:hidden}
body{position:relative;background:var(--white);font-family:var(--body);color:var(--text)}
.abs{position:absolute}

/* header */
.site-header{position:absolute;left:0;top:0;width:1200px;height:107px;background:var(--white)}
.brand{position:absolute;left:62px;top:24px;display:flex;align-items:center;gap:12px}
.brand-dot{width:50px;height:50px;border-radius:50%;background:var(--orange)}
.brand-name{font-family:var(--body);font-weight:700;font-size:25px;line-height:25px;color:#333;letter-spacing:.5px;width:120px}
.brand-tag{position:absolute;left:62px;top:82px;font-size:10px;color:#2a4d8f;font-weight:500}
.main-nav{position:absolute;left:375px;top:44px;display:flex;gap:0}
.main-nav a{font-size:17px;color:#555;text-decoration:none;text-transform:uppercase;position:absolute;white-space:nowrap}
.main-nav a.active{color:var(--ink);border-bottom:2px solid var(--ink);padding-bottom:6px}
.quote-btn{position:absolute;left:1003px;top:40px;width:137px;height:36px;background:var(--orange);color:var(--white);font-size:15px;font-weight:500;display:flex;align-items:center;justify-content:center}

/* hero */
.hero{position:absolute;left:0;top:107px;width:1200px;height:538px;background:radial-gradient(ellipse at 40% 50%,#2e2e2e 0%,#161616 70%,#0f0f0f 100%)}
.hero-art{position:absolute;left:100px;top:68px;width:560px;height:450px;border-radius:6px;background:linear-gradient(160deg,#3a3f48 0%,#23262c 60%,#2d4b66 100%)}
.hero-kicker{position:absolute;left:686px;top:103px;font-family:'Lato',sans-serif;font-weight:300;font-size:70px;color:var(--white);line-height:1}
.hero-title{position:absolute;left:684px;top:178px;font-family:'Oswald',sans-serif;font-weight:600;font-size:80px;color:var(--white);line-height:1;letter-spacing:.5px}
.hero-text{position:absolute;left:686px;top:278px;width:470px;font-size:16.5px;line-height:24px;color:#eee}
.hero-btn{position:absolute;left:686px;top:371px;width:137px;height:53px;background:var(--orange);color:var(--white);font-size:19px;font-weight:500;display:flex;align-items:center;justify-content:center;border-radius:2px}

/* section titles */
.sec-title{position:absolute;left:0;width:1200px;text-align:center;font-size:27px;font-weight:500;color:var(--ink);text-transform:uppercase}
.sec-sub{position:absolute;left:0;width:1200px;text-align:center;font-size:16px;color:#333;text-transform:uppercase}
.divider{position:absolute;left:525px;width:150px;height:4px;display:flex;gap:0}
.divider i{display:block;height:4px}

/* process */
.step{position:absolute;width:230px;text-align:center}
.step-circle{position:absolute;width:136px;height:136px;border-radius:50%;background:var(--orange);display:flex;align-items:center;justify-content:center}
.step-circle.first{background:#3a3a3a}
.step-num{position:absolute;width:36px;height:36px;border-radius:50%;background:var(--white);border:2px solid var(--orange);color:var(--orange);font-size:17px;display:flex;align-items:center;justify-content:center}
.step-label{position:absolute;width:200px;text-align:center;font-size:17px;line-height:20px;color:#333}

/* testimonials */
.testimonials{position:absolute;left:0;top:1066px;width:1200px;height:441px;background:var(--orange);overflow:hidden}
.testimonials .sec-title{color:var(--white)}
.quote-card{position:absolute;left:303px;top:116px;width:588px;height:145px;background:var(--white);border-radius:6px}
.quote-card::after{content:"";position:absolute;left:282px;bottom:-22px;border:22px solid transparent;border-bottom:0;border-top-color:var(--white)}
.quote-mark{position:absolute;font-family:Georgia,serif;font-size:54px;line-height:1;font-weight:700}
.quote-text{position:absolute;font-size:16px;line-height:29px;text-align:center}
.quote-card .quote-text{left:50px;top:27px;width:510px;color:#888}
.side-quote{position:absolute;color:var(--white);font-size:16px;line-height:29px}
.reviewer{position:absolute;text-align:center;color:var(--white)}
.reviewer b{display:block;font-weight:400;font-size:16px}
.reviewer span{display:block;font-size:12px;margin-top:6px}
.slider-dots{position:absolute;left:565px;top:390px;display:flex;gap:6px}
.slider-dots i{display:block;width:18px;height:3px;background:#f2a37f}
.slider-dots i.on{background:var(--white)}

/* about */
.about-title{color:var(--orange)}
.offer-heading{position:absolute;left:55px;top:1662px;font-size:25px;font-weight:500;color:var(--orange);text-transform:uppercase}
.offer-text{position:absolute;left:55px;top:1700px;width:675px;font-size:15.5px;line-height:23.5px;color:#333}
.service-list{position:absolute;list-style:none}
.service-list li{position:absolute;display:flex;align-items:center;gap:14px;font-size:15.5px;color:#333;white-space:nowrap}
.service-list svg{width:28px;height:28px;flex:none}
.small-btn{position:absolute;left:55px;top:2001px;width:97px;height:29px;background:var(--orange);color:var(--white);font-size:11px;font-weight:700;display:flex;align-items:center;justify-content:center;text-transform:uppercase}
.exploded-art{position:absolute;left:754px;top:1617px;width:284px;height:423px;border-radius:10px;background:linear-gradient(160deg,#2b2b2b 0%,#555 35%,#3c8a5c 60%,#c9a35a 80%,#2a2a2a 100%)}

/* map + contact */
.map{position:absolute;left:0;top:2077px;width:1200px;height:505px;background:linear-gradient(135deg,#7a7a7a 0%,#666 50%,#737373 100%);border-top:4px solid var(--orange)}
.map-pin{position:absolute;left:404px;top:2120px}
.contact-card{position:absolute;left:612px;top:2238px;width:294px;height:277px;background:var(--white)}
.contact-card::before{content:"";position:absolute;left:-20px;top:38px;border:20px solid transparent;border-left:0;border-right-color:var(--white)}
.contact-card h4{position:absolute;left:40px;font-size:15px;font-weight:500;color:var(--orange);text-transform:uppercase}
.contact-card p{position:absolute;left:40px;font-size:13.5px;line-height:21px;color:#555}

/* footer */
.footer-nav{position:absolute;top:2622px;left:0;width:1200px}
.footer-nav a{position:absolute;font-size:14px;color:#666;text-decoration:none;transform:translateX(-50%);white-space:nowrap}
.footer-nav a.active{color:var(--orange)}
.footer-rule{position:absolute;left:52px;top:2657px;width:1088px;height:1px;background:var(--rule)}
.copyright{position:absolute;left:52px;top:2686px;font-size:14px;color:#555}
.copyright em{font-style:normal;color:var(--orange)}
.socials{position:absolute;left:880px;top:2677px;display:flex;gap:17px}
.socials i{display:block;width:30px;height:30px;border-radius:50%;background:#a9a9a9}
.socials i.on{background:var(--orange);box-shadow:0 0 0 3px #f6c9b5}
</style>
</head>
<body>

<header class="site-header">
  <div class="brand"><span class="brand-dot"></span><span class="brand-name">GADGET HAVEN</span></div>
  <span class="brand-tag">We will come to you!</span>
  <nav class="main-nav">
    <a class="active" href="#" style="left:0">Home</a>
    <a href="#" style="left:99px">About Us</a>
    <a href="#" style="left:232px">Device Repairs</a>
    <a href="#" style="left:417px">FAQ</a>
    <a href="#" style="left:496px">Contact</a>
  </nav>
  <div class="quote-btn">Request Quote</div>
</header>

<section class="hero">
  <div class="hero-art" role="img" aria-label="Group of smartphones and a tablet with cracked screens, one splashing in water"></div>
  <div class="hero-kicker">We Repair</div>
  <h1 class="hero-title">MOBILE PHONE</h1>
  <p class="hero-text">The kind of services we provide are, among other things, installations of hardware and software and the repair of broken or malfunctioning devices.</p>
  <div class="hero-btn">Read More</div>
</section>

<!-- process -->
<h2 class="sec-title" style="top:685px">The Process</h2>
<div class="divider" style="top:729px"><i style="width:62px;background:#333"></i><i style="width:26px;background:var(--orange)"></i><i style="width:62px;background:#333"></i></div>
<p class="sec-sub" style="top:755px">How to repair your mobile device</p>

<svg class="abs" style="left:0;top:790px" width="1200" height="60" viewBox="0 0 1200 60" fill="none">
  <g stroke="var(--orange)" stroke-width="3" stroke-dasharray="1 9" stroke-linecap="round">
    <path d="M175 40 Q255 0 320 40"/><path d="M405 40 Q485 0 550 40"/>
    <path d="M636 40 Q716 0 781 40"/><path d="M868 40 Q948 0 1013 40"/>
  </g>
  <g fill="var(--orange)">
    <path d="M320 40 l-9 -2 l5 -6z"/><path d="M550 40 l-9 -2 l5 -6z"/>
    <path d="M781 40 l-9 -2 l5 -6z"/><path d="M1013 40 l-9 -2 l5 -6z"/>
  </g>
</svg>

<div class="step-circle first" style="left:68px;top:832px">
  <svg width="70" height="70" viewBox="0 0 70 70" fill="none" stroke="#fff" stroke-width="3"><rect x="22" y="8" width="28" height="52" rx="4"/><circle cx="30" cy="30" r="9"/><path d="M24 37 l-10 12"/></svg>
</div>
<div class="step-num" style="left:174px;top:849px">1</div>
<div class="step-label" style="left:36px;top:982px">Choose your device and repair job</div>

<div class="step-circle" style="left:298px;top:832px">
  <svg width="70" height="70" viewBox="0 0 70 70" fill="#fff"><path d="M30 18 L10 35 L30 52 V42 C44 42 54 46 62 56 C58 38 48 28 30 28Z"/><path d="M22 18 L2 35 L22 52 V46 L10 35 L22 24Z"/></svg>
</div>
<div class="step-num" style="left:404px;top:849px">2</div>
<div class="step-label" style="left:266px;top:982px">Place the<br>order</div>

<div class="step-circle" style="left:529px;top:832px">
  <svg width="70" height="70" viewBox="0 0 70 70" fill="none" stroke="#fff" stroke-width="3.5"><path d="M14 38 V32 A21 21 0 0 1 56 32 V38"/><rect x="9" y="34" width="10" height="16" rx="4" fill="#fff"/><rect x="51" y="34" width="10" height="16" rx="4" fill="#fff"/><path d="M56 50 Q54 60 40 60"/></svg>
</div>
<div class="step-num" style="left:635px;top:849px">3</div>
<div class="step-label" style="left:497px;top:982px">Get a callback<br>within the hour</div>

<div class="step-circle" style="left:761px;top:832px">
  <svg width="70" height="70" viewBox="0 0 70 70"><path d="M35 8 C25 8 19 15 19 24 C19 36 35 50 35 50 C35 50 51 36 51 24 C51 15 45 8 35 8Z" fill="#fff"/><circle cx="35" cy="24" r="6" fill="var(--orange)"/><path d="M10 58 H60 M16 52 L10 58 M54 52 L60 58" stroke="#fff" stroke-width="3" fill="none"/></svg>
</div>
<div class="step-num" style="left:867px;top:849px">4</div>
<div class="step-label" style="left:729px;top:982px">Set date and<br>Location</div>

<div class="step-circle" style="left:991px;top:832px">
  <svg width="70" height="70" viewBox="0 0 70 70" fill="none" stroke="#fff" stroke-width="3"><rect x="25" y="12" width="20" height="44" rx="3"/><path d="M17 24 Q12 34 17 44 M10 19 Q2 34 10 49 M53 24 Q58 34 53 44 M60 19 Q68 34 60 49"/></svg>
</div>
<div class="step-num" style="left:1097px;top:849px">5</div>
<div class="step-label" style="left:959px;top:982px">We will come<br>to you.</div>

<!-- testimonials -->
<section class="testimonials">
  <h2 class="sec-title" style="top:38px">Testimonials</h2>
  <div class="divider" style="top:82px"><i style="width:62px;background:#222"></i><i style="width:26px;background:#fff"></i><i style="width:62px;background:#222"></i></div>

  <div class="side-quote" style="left:0;top:143px;width:240px">andit odio. Phasellus lectus nisi,<br>or ut nibh. Nunc eu lacus blandit,<br>in in nisl velit. Praesent fringilla</div>
  <div class="reviewer" style="left:-10px;top:310px;text-align:left"><b>ssim</b><span>ame</span></div>

  <div class="quote-card">
    <span class="quote-mark" style="left:26px;top:20px;color:#999">“</span>
    <p class="quote-text">Lorem ipsum dolor sit amet, consectetur adipiscing elit. Curabitur aliquam quam ut massa volutpat interdum. Morbi vel metus cursus purus iaculis blandit pharetra vel lorem.+</p>
  </div>
  <div class="reviewer" style="left:448px;top:308px;width:300px"><b>Vivamusips Erapulvinar</b><span>Customer Name</span></div>

  <span class="quote-mark" style="left:948px;top:136px;color:#f5b08f">“</span>
  <div class="side-quote" style="left:998px;top:143px;width:260px;white-space:nowrap">Nullam laoreet enim ante, e<br>suada dignissim ante, at lo<br>&nbsp;&nbsp;&nbsp;&nbsp;&nbsp;quamlacinia sit amet</div>
  <div class="reviewer" style="left:1148px;top:310px;text-align:left"><b>Malesu</b><span>Custo</span></div>

  <div class="slider-dots"><i class="on"></i><i></i><i></i></div>
</section>

<!-- who we are -->
<h2 class="sec-title about-title" style="top:1550px">Who We Are?</h2>
<div class="divider" style="top:1593px"><i style="width:62px;background:#777"></i><i style="width:26px;background:var(--orange)"></i><i style="width:62px;background:#777"></i></div>
<p class="sec-sub" style="top:1611px;font-size:15px">Some things you should know about us</p>

<h3 class="offer-heading">We offer a full range of smartphone services</h3>
<p class="offer-text">Our company is based in Rotterdam, the Netherlands. We provide different services for all kinds of electronic devices. The kind of services we provide are, among other things, installations of hardware and software and the repair of broken or malfunctioning devices.</p>

<ul class="service-list" style="left:55px;top:0">
  <li style="top:1800px"><svg viewBox="0 0 28 28" fill="none" stroke="#333" stroke-width="1.6"><rect x="8" y="2" width="12" height="24" rx="2"/><circle cx="14" cy="13" r="3"/></svg>Phone Diagnosis</li>
  <li style="top:1846px"><svg viewBox="0 0 28 28" fill="none" stroke="#333" stroke-width="1.6"><path d="M10 4 C6 10 4 13 4 16 a6 6 0 0 0 12 0 C16 13 14 10 10 4Z"/><path d="M18 14 l6 -6 M20 20 l6 -4"/></svg>Water Damaged Phone</li>
  <li style="top:1892px"><svg viewBox="0 0 28 28" fill="none" stroke="#333" stroke-width="1.6"><rect x="7" y="2" width="14" height="24" rx="2"/><path d="M7 21 H21"/></svg>LCD Display Replacement</li>
  <li style="top:1940px"><svg viewBox="0 0 28 28" fill="none" stroke="#333" stroke-width="1.6"><rect x="8" y="5" width="12" height="21" rx="2"/><path d="M12 2 H16 V5 M15 10 l-3 5 h4 l-3 5"/></svg>Battery Replacement</li>
</ul>
<ul class="service-list" style="left:316px;top:0">
  <li style="top:1800px"><svg viewBox="0 0 28 28" fill="none" stroke="#333" stroke-width="1.6"><path d="M3 7 H11 L13 10 H25 V23 H3Z M3 13 H25"/></svg>Data Recovery</li>
  <li style="top:1846px"><svg viewBox="0 0 28 28" fill="none" stroke="#333" stroke-width="1.6"><path d="M5 18 V14 a9 9 0 0 1 18 0 V18"/><rect x="3" y="16" width="5" height="9" rx="2"/><rect x="20" y="16" width="5" height="9" rx="2"/></svg>Ear Phone Jack Malfunctions</li>
  <li style="top:1892px"><svg viewBox="0 0 28 28" fill="none" stroke="#333" stroke-width="1.6"><rect x="4" y="3" width="20" height="14"/><path d="M4 21 H24 M4 25 H24 M14 6 V13 M11 10 l3 3 l3 -3"/></svg>Installations</li>
  <li style="top:1940px"><svg viewBox="0 0 28 28" fill="none" stroke="#333" stroke-width="1.6"><rect x="4" y="10" width="20" height="14"/><rect x="9" y="14" width="10" height="6"/><path d="M8 10 V5 M14 10 V5 M20 10 V5"/></svg>Hardware and Software</li>
</ul>
<div class="small-btn">Read More</div>
<div class="exploded-art" role="img" aria-label="Exploded view of a smartphone showing screen, frame, circuit board and battery layers"></div>

<!-- map + contact -->
<section class="map" role="img" aria-label="Greyscale street map of the Rotterdam area"></section>
<svg class="map-pin" width="92" height="114" viewBox="0 0 92 114"><path d="M46 4 C22 4 4 22 4 46 C4 70 46 110 46 110 C46 110 88 70 88 46 C88 22 70 4 46 4Z" fill="var(--orange)" stroke="#fff" stroke-width="4"/><circle cx="46" cy="46" r="22" fill="#fff"/></svg>
<div class="contact-card">
  <h4 style="top:40px">Address</h4>
  <p style="top:65px">48 Havenkade Street<br>&nbsp;Rotterdam, Netherlands</p>
  <h4 style="top:130px">Email</h4>
  <p style="top:156px">info@gadgethaven.com</p>
  <h4 style="top:201px">Phone</h4>
  <p style="top:228px">(010) 555 0147</p>
</div>

<!-- footer -->
<footer>
  <nav class="footer-nav">
    <a class="active" href="#" style="left:398px">Home</a>
    <a href="#" style="left:491px">About Us</a>
    <a href="#" style="left:618px">Devices Repairs</a>
    <a href="#" style="left:729px">FAQ</a>
    <a href="#" style="left:811px">Contact</a>
  </nav>
  <div class="footer-rule"></div>
  <p class="copyright">© 2017 <em>Gadget Haven</em>. All Rights Reserved.</p>
  <div class="socials" aria-label="Social media links"><i class="on"></i><i></i><i></i><i></i><i></i><i></i></div>
</footer>

</body>
</html>
```